PowerPoint Template - Multiple Slide Backgrounds

Looking for a professional PowerPoint template for a technology company. You will see with the logo there's sort of a theme with gears and a lightbulb of sorts. Keeping with this sort of design could help with the brand.

Branding information
• Logo with transparent background included
• Primary Color (Orange) Hex #E6753D
• Secondary Color (Brown) Hex #6A4238
• Primary Font - Myriad Pro
• Secondary Font - Quiet Sans Light

Design request -
• PowerPoint (POTX) template with master slide views
• Cover Slide
• Color Pallet - 7 Color PowerPoint pallet that includes and complements primary and secondary colors
• Slide Master with Footer
• Multiple Background Types to allow for smart art overlay or bullet point text boxes
Bonus - Sample graphical elements using shapes and smart art

```html
<!DOCTYPE html>
<html lang="en">
<head>
<meta charset="utf-8">
<title>Lakeside DevWorks – Slide Template, First Part</title>
<link rel="stylesheet" href="https://fonts.googleapis.com/css2?family=Signika:wght@400;600;700&family=Source+Sans+3:wght@300;400;600;700&display=swap">
<style>
:root{
  --orange:#e6753d;
  --orange-soft:#f0a070;
  --peach:#f6c8a8;
  --brown:#6a4238;
  --brown-dark:#5a3328;
  --ink:#4a4a4a;
  --footer:#5b5b5b;
  --page:#ebebeb;
  --caption:#1b5a8f;
  --white:#ffffff;
}
*{box-sizing:border-box;margin:0;padding:0}
html,body{width:1200px;height:1050px;overflow:hidden;background:var(--page)}
body{position:relative;font-family:"Source Sans 3",Arial,sans-serif;color:var(--ink)}
.slide{position:absolute;overflow:hidden;background:var(--white)}
.heading{font-family:"Signika",Arial,sans-serif;font-weight:600;color:var(--brown);line-height:1.12}
.brand{position:absolute;display:flex;align-items:center;gap:4px;font-family:"Source Sans 3",Arial,sans-serif;font-weight:700;color:var(--brown);white-space:nowrap}
.brand-dot{border-radius:50%;border:2px solid var(--orange);flex:none}
.brand--light{color:var(--white)}
.photo{position:absolute}
.footer-bar{position:absolute;left:0;right:0;bottom:0;height:17px;background:var(--footer);color:var(--white);font-size:6px;font-weight:600;padding:6px 0 0 17px}
.page-tab{position:absolute;right:0;bottom:0;width:44px;height:23px;background:var(--brown-dark);clip-path:polygon(18% 0,100% 0,100% 100%,0 100%);color:var(--white);font-size:7px;font-weight:600;text-align:center;padding-top:9px;padding-left:6px}
.body-copy{font-size:8.4px;line-height:1.35;color:var(--ink)}

/* slide 1 */
.s1{left:21px;top:13px;width:555px;height:312px}
.s1 .title{position:absolute;left:28px;top:150px;font-size:27px;font-weight:700}
.s1 .subtitle{position:absolute;left:28px;top:221px;font-size:11px;color:var(--ink)}

/* slide 2 */
.s2{left:618px;top:13px;width:556px;height:312px}
.s2 .band{position:absolute;left:0;top:214px;width:390px;height:98px;background:var(--orange)}
.s2 .title{position:absolute;left:18px;top:228px;font-size:24px;font-weight:700;color:var(--white);text-transform:uppercase;line-height:1.15}
.s2 .subtitle{position:absolute;left:18px;top:285px;font-size:10px;color:var(--white)}
.s2 .logo-panel{position:absolute;left:390px;top:232px;width:166px;height:80px;background:rgba(245,245,245,.92)}

/* slide 3 */
.s3{left:21px;top:335px;width:557px;height:313px;background:#333}
.s3 .title{position:absolute;left:18px;top:176px;font-size:28px;font-weight:700;color:var(--white);text-transform:uppercase}
.s3 .sub-bar{position:absolute;left:18px;top:220px;width:282px;height:17px;background:var(--orange);color:var(--white);font-size:7px;padding:4px 0 0 5px}
.s3 .body-copy{position:absolute;left:18px;top:246px;width:260px;color:var(--white);font-size:7.6px}

/* slide 4 */
.s4{left:618px;top:335px;width:556px;height:311px}
.s4 .title{position:absolute;left:18px;top:19px;font-size:21px}
.s4 .feature{position:absolute;left:367px;top:51px;width:189px;height:141px;background:var(--orange);color:var(--white);padding:18px 16px}
.s4 .feature h3{font-size:9.5px;font-weight:700;text-transform:uppercase;line-height:1.25;margin-top:14px}
.s4 .feature p{font-size:7.6px;line-height:1.3;margin-top:3px}
.s4 .lead{position:absolute;left:28px;top:213px;font-size:15px}
.s4 .body-copy{position:absolute;left:155px;top:218px;width:388px}

/* slide 5 */
.s5{left:21px;top:660px;width:556px;height:312px}
.s5 .title{position:absolute;left:332px;top:78px;font-size:21px}
.s5 .rule{position:absolute;left:332px;top:141px;width:95px;height:2px;background:var(--orange)}
.s5 .body-copy{position:absolute;left:332px;top:157px;width:200px}

/* slide 6 */
.s6{left:618px;top:662px;width:557px;height:313px}
.s6 .title{position:absolute;left:18px;top:20px;font-size:21px}
.s6 .rule{position:absolute;left:18px;top:51px;width:88px;height:2px;background:var(--orange)}
.s6 .label{position:absolute;font-size:8px;font-weight:600;color:var(--orange);line-height:1.15}
.s6 .label span{display:block;font-size:6px;font-weight:400;color:var(--ink)}
.s6 .label--right{text-align:right}

.caption{position:absolute;left:18px;top:990px;font-family:Arial,Helvetica,sans-serif;font-weight:700;font-size:44px;color:var(--caption);letter-spacing:.3px}
</style>
</head>
<body>

<!-- Cover option 1 -->
<section class="slide s1">
  <svg width="555" height="312" viewBox="0 0 555 312" style="position:absolute;left:0;top:0">
    <defs>
      <linearGradient id="teamTone" x1="0" y1="0" x2="1" y2="1">
        <stop offset="0" stop-color="#c9d8e8"/>
        <stop offset=".5" stop-color="#7f9fc0"/>
        <stop offset="1" stop-color="#2f4f78"/>
      </linearGradient>
    </defs>
    <rect x="200" y="0" width="355" height="312" fill="url(#teamTone)" role="img" aria-label="Photo of a team working together around a tablet"/>
    <circle cx="-70" cy="160" r="345" fill="#ffffff"/>
    <path d="M205 0 A345 345 0 0 1 270 312" fill="none" stroke="#6a4238" stroke-width="20"/>
    <path d="M250 82 A300 300 0 0 1 218 312" fill="none" stroke="#e6753d" stroke-width="16"/>
  </svg>
  <div class="brand" style="left:28px;top:72px;font-size:10px"><span class="brand-dot" style="width:10px;height:10px"></span>Lakeside DevWorks</div>
  <h1 class="heading title">Presentation<br>Title Option 1</h1>
  <p class="subtitle">Subtitle</p>
</section>

<!-- Cover option 2 -->
<section class="slide s2">
  <div class="photo" role="img" aria-label="Greyscale photo of hands using a transparent digital display" style="left:0;top:0;width:556px;height:312px;background:linear-gradient(135deg,#d8d8d8,#8a8a8a 55%,#4a4a4a)"></div>
  <div class="band"></div>
  <h1 class="heading title">Presentation Title<br>Option 2</h1>
  <p class="subtitle">Subtitle</p>
  <div class="logo-panel">
    <div class="brand" style="left:28px;top:33px;font-size:10px"><span class="brand-dot" style="width:10px;height:10px"></span>Lakeside DevWorks</div>
  </div>
</section>

<!-- Cover option 3 -->
<section class="slide s3">
  <div class="photo" role="img" aria-label="Dark greyscale photo of hands with a tablet and technology graphics" style="left:0;top:0;width:557px;height:313px;background:linear-gradient(160deg,#8a8a8a,#4b4b4b 45%,#1e1e1e)"></div>
  <div class="brand brand--light" style="left:440px;top:58px;font-size:11px"><span class="brand-dot" style="width:11px;height:11px;border-color:#fff"></span>Lakeside DevWorks</div>
  <h1 class="heading title">Presentation Title Option 3</h1>
  <div class="sub-bar">Subtitle</div>
  <p class="body-copy">In mauris justo, condimentum non ligula id, scelerisque tempor augue.<br>In a nibh vitae augue accumsan cursus sit amet accumsan enim.<br>Praesent et luctus purus.</p>
</section>

<!-- Content: Creative -->
<section class="slide s4">
  <h2 class="heading title">Creative</h2>
  <div class="brand" style="left:476px;top:30px;font-size:6px"><span class="brand-dot" style="width:7px;height:7px;border-width:1.5px"></span>Lakeside DevWorks</div>
  <div class="photo" role="img" aria-label="Photo of colleagues talking around a table" style="left:0;top:51px;width:367px;height:141px;background:linear-gradient(90deg,#8c8a84,#cfc9bf 45%,#a79f92 75%,#6f6a62)"></div>
  <div class="feature">
    <svg width="30" height="28" viewBox="0 0 30 28" fill="none" stroke="#fff" stroke-width="1.6">
      <rect x="2" y="2" width="26" height="18" rx="1.5"/>
      <line x1="6" y1="8" x2="24" y2="8"/><line x1="6" y1="12" x2="18" y2="12"/>
      <line x1="15" y1="20" x2="15" y2="25"/><line x1="9" y1="26" x2="21" y2="26"/>
    </svg>
    <h3>Lorem ipsum dolor<br>sit amet</h3>
    <p>Adipiscing elit. In mauris justo, condimentum non ligula id, scelerisque tempor augue.</p>
  </div>
  <h3 class="heading lead">Lorem ipsum<br>dolor sit</h3>
  <p class="body-copy">Lorem ipsum dolor sit amet, consectetur adipiscing elit. In mauris justo, condimentum non ligula id, scelerisque tempor augue. In a nibh vitae augue accumsan cursus sit amet accumsan enim. Praesent et luctus purus. Donec non risus molestie dui viverra ultricies sed in ligula.</p>
  <div class="footer-bar">Footer</div>
  <div class="page-tab">4</div>
</section>

<!-- Content: Smart devices -->
<section class="slide s5">
  <div class="brand" style="left:478px;top:34px;font-size:6px"><span class="brand-dot" style="width:7px;height:7px;border-width:1.5px"></span>Lakeside DevWorks</div>
  <div class="photo" role="img" aria-label="Laptop mockup showing a businessman touching a digital interface" style="left:0;top:38px;width:350px;height:232px;background:linear-gradient(100deg,#5f86b0,#2c4d78 55%,#1a2d4a 80%,#cfd3d8 92%,#f2f2f2)"></div>
  <h2 class="heading title">Smart Devices<br>Mockup</h2>
  <div class="rule"></div>
  <p class="body-copy">Lorem ipsum dolor sit amet, consectetur adipiscing elit. In mauris justo, condimentum non ligula id, scelerisque tempor augue. In a nibh vitae augue accumsan cursus sit amet accumsan enim.</p>
  <div class="footer-bar">Footer</div>
  <div class="page-tab">5</div>
</section>

<!-- Content: Diagram -->
<section class="slide s6">
  <h2 class="heading title">Diagram</h2>
  <div class="rule"></div>
  <div class="brand" style="left:476px;top:32px;font-size:6px"><span class="brand-dot" style="width:7px;height:7px;border-width:1.5px"></span>Lakeside DevWorks</div>
  <svg width="557" height="313" viewBox="0 0 557 313" style="position:absolute;left:0;top:0">
    <g fill="none" stroke-width="30">
      <path d="M268 93 A77 77 0 0 1 345 170" stroke="#6a4238"/>
      <path d="M345 170 A77 77 0 0 1 268 247" stroke="#e6753d"/>
      <path d="M268 247 A77 77 0 0 1 191 170" stroke="#f0a070"/>
      <path d="M191 170 A77 77 0 0 1 268 93" stroke="#f6c8a8"/>
    </g>
    <g stroke="#e6753d" stroke-width="3" fill="none">
      <line x1="268" y1="78" x2="268" y2="108" stroke="#fff"/>
      <line x1="268" y1="232" x2="268" y2="262" stroke="#fff"/>
      <line x1="176" y1="170" x2="206" y2="170" stroke="#fff"/>
      <line x1="330" y1="170" x2="360" y2="170" stroke="#fff"/>
    </g>
    <g stroke="#b5b5b5" stroke-width=".8" fill="none">
      <polyline points="134,91 175,91 206,115"/>
      <polyline points="400,91 360,91 330,115"/>
      <polyline points="134,251 175,251 206,225"/>
      <polyline points="400,251 360,251 330,225"/>
    </g>
    <g fill="#9a9a9a">
      <circle cx="134" cy="91" r="1.6"/><circle cx="400" cy="91" r="1.6"/>
      <circle cx="134" cy="251" r="1.6"/><circle cx="400" cy="251" r="1.6"/>
    </g>
  </svg>
  <div class="brand" style="left:223px;top:182px;font-size:9.5px"><span class="brand-dot" style="width:9px;height:9px"></span>Lakeside DevWorks</div>
  <div class="label label--right" style="right:434px;top:84px">Identify<span>Lorem ipsum dolor sit</span></div>
  <div class="label" style="left:411px;top:84px">Analyze<span>Lorem ipsum dolor sit</span></div>
  <div class="label label--right" style="right:434px;top:244px">Measure<span>Lorem ipsum dolor sit</span></div>
  <div class="label" style="left:411px;top:244px">Create<span>Lorem ipsum dolor sit</span></div>
  <div class="footer-bar">Footer</div>
  <div class="page-tab">6</div>
</section>

<p class="caption">Lakeside DevWorks - First Part</p>

</body>
</html>
```